Copperfield Roofing Co. business card design

I am a Roofing contractor in Texas. The name of my company is Copperfield Roofing Co. I also offer a few other services (Christmas light installation, gutters, fencing, pressure washing). However my main gig is roofing. Storm restoration and knowledge of the insurance claim process is my specialty.

My colors are black, red and white. I’d like something pretty simple and clean. Modern looking but with a splash of this red tartan pattern.

I have another version of my logo being edited at the moment where the little top part of the F in roofing that’s currently tartan will be changed to just solid red to make it more visible. So if that’s something you can change in your mock up great. But I can provide the full version once the contest is complete

Target Market(s)

Homeowners

Industry/Entity Type

Roofing

Contact Information for Business Card

Derek Pruitt. 682-555-0193. www.copperfield roofing.co Derek@copperfieldroofing.co

Colors
EB3D1F
EC4F4E
F09395
F8D3D4
FCEDEE

Requirements
Nice to have
• Maybe instead of a business address. I could say serving all DFW Texas or something like that. And maybe add a line somewhere saying deductible assistance? Just a thought

```html
<!DOCTYPE html>
<html lang="en">
<head>
<meta charset="utf-8">
<title>Copperfield Roofing Co. — Business Card</title>
<link href="https://fonts.googleapis.com/css2?family=Saira:wght@600;800&family=Open+Sans:wght@400;600&display=swap" rel="stylesheet">
<style>
  :root {
    --stage: #2b2d31;
    --card: #141414;
    --red: #e02a2a;
    --red-deep: #b51d1f;
    --white: #ffffff;
    --grey: #d6d6d6;
  }
  * { box-sizing: border-box; margin: 0; padding: 0; }
  html, body {
    width: 1200px; height: 900px; overflow: hidden;
    background: var(--stage);
  }
  .stage {
    width: 1200px; height: 900px;
    display: flex; align-items: center; justify-content: center; gap: 40px;
  }
  .card {
    position: relative;
    width: 540px; height: 309px;
    background: var(--card);
    border-radius: 20px;
    box-shadow: 0 14px 30px rgba(0,0,0,.45);
    overflow: hidden;
  }

  /* contact side */
  .contact-block { position: absolute; left: 40px; top: 36px; width: 270px; }
  .person-name {
    font-family: "Saira", sans-serif; font-weight: 800;
    font-size: 24px; letter-spacing: .5px; line-height: 1;
    color: var(--red); text-transform: uppercase;
  }
  .person-title {
    font-family: "Open Sans", sans-serif; font-weight: 600;
    font-size: 13px; color: var(--grey); margin-top: 4px;
  }
  .divider { width: 14px; height: 2px; background: var(--red-deep); margin: 22px 0 20px; }
  .contact-list { list-style: none; }
  .contact-list li {
    display: flex; align-items: center; gap: 9px;
    font-family: "Open Sans", sans-serif; font-size: 13px;
    color: var(--grey); line-height: 1.75; white-space: nowrap;
  }
  .contact-list svg { width: 10px; height: 10px; flex: none; fill: var(--red); }

  .brand {
    display: flex; flex-direction: column; align-items: center; gap: 10px;
  }
  .brand-mark {
    width: 78px; height: 78px; border-radius: 50%;
    background: var(--red);
    border: 4px solid var(--white);
    flex: none;
  }
  .brand-name {
    font-family: "Saira", sans-serif; font-weight: 800;
    font-size: 22px; line-height: 1.05; color: var(--white);
    text-transform: uppercase; letter-spacing: 1px; text-align: center;
  }
  .card-front .brand { position: absolute; right: 36px; bottom: 28px; }

  /* logo side */
  .card-back {
    display: flex; flex-direction: column; align-items: center; justify-content: center; gap: 16px;
  }
  .service-area {
    font-family: "Open Sans", sans-serif; font-size: 14px;
    color: var(--white); letter-spacing: .3px;
  }
</style>
</head>
<body>
<main class="stage">

  <section class="card card-front">
    <div class="contact-block">
      <h1 class="person-name">Derek Pruitt</h1>
      <p class="person-title">CEO/Founder</p>
      <div class="divider"></div>
      <ul class="contact-list">
        <li>
          <svg viewBox="0 0 24 24" aria-hidden="true"><path d="M6.6 10.8a15.1 15.1 0 0 0 6.6 6.6l2.2-2.2c.3-.3.7-.4 1-.2 1.1.4 2.3.6 3.6.6.6 0 1 .4 1 1V20c0 .6-.4 1-1 1A17 17 0 0 1 3 4c0-.6.4-1 1-1h3.5c.6 0 1 .4 1 1 0 1.3.2 2.5.6 3.6.1.3 0 .7-.2 1z"/></svg>
          682-555-0193
        </li>
        <li>
          <svg viewBox="0 0 24 24" aria-hidden="true"><path d="M2 5h20v14H2z M2 5l10 8 10-8" /></svg>
          Derek@copperfieldroofing.co
        </li>
        <li>
          <svg viewBox="0 0 24 24" aria-hidden="true"><circle cx="12" cy="12" r="10"/></svg>
          www.copperfield roofing.co
        </li>
      </ul>
    </div>
    <div class="brand">
      <div class="brand-mark"></div>
      <p class="brand-name">Copperfield<br>Roofing Co.</p>
    </div>
  </section>

  <section class="card card-back">
    <div class="brand">
      <div class="brand-mark"></div>
      <p class="brand-name">Copperfield<br>Roofing Co.</p>
    </div>
    <p class="service-area">Serving all DFW Texas</p>
  </section>

</main>
</body>
</html>
```